Letterhead Design Project

I need a simple, clean and corporate letterhead & follow-on letterhead.
The follow-on letterhead should just have the logo only.
Final File Specs:
Full Bleed Size (starting document size)
213 x 300 mm
2517 x 3544 pixels
* Finished artwork should use the full bleed dimensions for best results.
Document Trim Size (final size after being cut)
210 x 297 mm
2480 x 3508 pixels
* Please be sure to keep all text within the safe margin.
Resolution 300 DPI
Accepted file types:-
Adobe Acrobat 9 Document (*.pdf) (recommended)
Adobe Illustrator CS3 Artwork (*.ai) (recommended)
Adobe Photoshop CS3 Image (*.psd) (recommended)
Bitmap Image (*.bmp)
GIF Image (*.gif)
JPEG Image (*.jpg,*.jpeg)
Microsoft PowerPoint 2010 Document (*.ppt)
Microsoft Publisher 2010 Document (*.pub)
Microsoft Word 2010 Document (*.doc)
PCX Image (*.pcx)
PICT Image (*.pic,*.pict,*.pct)
PNG Image (*.png)
PostScript Document (*.ps)
TIF Image (*.tif,*.tiff)
Windows Enhanced Metafile (*.emf)
Windows Metafile (*.wmf)
Requirements
Must have
- My letterhead must have:-
- Logo
- ACN - 482 617 309
- address - Suite 8, 51 Hartwell Ave, Marrowby, NSW 2047
- phone - (02) 8371 5926
- fax - (02) 8352 6149
- email - info@brantorguard.com.au
- web - www.brantorguard.com.au
Follow-on letterhead should have the logo only

```html
<!DOCTYPE html>
<html lang="en">
<head>
<meta charset="utf-8">
<title>Brantor Guard Letterhead</title>
<link href="https://fonts.googleapis.com/css2?family=Source+Sans+3:wght@400;700&display=swap" rel="stylesheet">
<style>
  :root {
    --backdrop: #2a2a2a;
    --paper: #ffffff;
    --brand-green: #b0d03f;
    --brand-navy: #2e2b5c;
    --ink: #1e1e1e;
    --footer-text: #f4f8e6;
  }
  * { margin: 0; padding: 0; box-sizing: border-box; }
  html, body { width: 1200px; height: 1000px; overflow: hidden; }
  body {
    background: var(--backdrop);
    font-family: "Source Sans 3", Arial, sans-serif;
    position: relative;
  }
  .sheet {
    position: absolute;
    background: var(--paper);
    width: 477px;
    height: 675px;
    box-shadow: 0 2px 8px rgba(0,0,0,.45);
  }
  .sheet--first { left: 113px; top: 127px; }
  .sheet--follow { left: 632px; top: 130px; width: 475px; height: 671px; }

  .brand {
    position: absolute;
    left: 30px; top: 32px;
    display: flex; align-items: center; gap: 9px;
  }
  .brand__mark {
    width: 26px; height: 26px;
    background: var(--brand-navy);
    border-radius: 3px;
  }
  .brand__name {
    font-size: 30px; font-weight: 700;
    color: var(--brand-green);
    letter-spacing: -0.3px;
    line-height: 1;
  }

  .address {
    position: absolute;
    left: 373px; top: 23px;
    font-size: 11px; line-height: 14px;
    color: var(--brand-navy);
    font-style: normal;
  }
  .address__label { color: var(--brand-green); }

  .letter {
    position: absolute;
    left: 30px; top: 128px;
    width: 410px;
    font-size: 8.7px; line-height: 11.3px;
    color: var(--ink);
  }
  .letter__salutation { margin-bottom: 10px; }
  .letter p + p.letter__new-block { margin-top: 11px; }
  .letter__sign { margin-top: 22px; margin-left: 2px; }

  .footer {
    position: absolute; left: 0; right: 0; bottom: 0;
  }
  .footer__rule { height: 5px; background: var(--brand-navy); }
  .footer__band {
    margin-top: 2px;
    height: 65px;
    background: var(--brand-green);
    padding: 4px 0 0 22px;
    color: var(--footer-text);
    font-size: 9.5px; line-height: 11.5px;
  }
  .sheet--follow .footer__band { height: 63px; }
  .contact { display: flex; align-items: center; gap: 5px; }
  .contact svg { width: 8px; height: 8px; flex: none; }
  .contact--plain { padding-left: 13px; }
</style>
</head>
<body>

<section class="sheet sheet--first" aria-label="First page letterhead">
  <div class="brand">
    <span class="brand__mark"></span>
    <span class="brand__name">Brantor Guard</span>
  </div>

  <address class="address">
    <span class="address__label">Address:</span><br>
    Suite 8,<br>51 Hartwell Ave,<br>Marrowby,<br>NSW 2047
  </address>

  <div class="letter">
    <p class="letter__salutation">Dear Addressee Name:</p>
    <p>Andipsum dipsum nostis nulpute magnissis niatie te molor adignis sequips uscipisit, sit vel ipsuscing ent lut lan ulla feugait augueraesto odolore doluptatio cons dolor sismodo luptatuero do od dolore magnim dolor auguero eu facilis ea core estrud eugiat velis ad tat dio odolor augue magna corting eugait enim venibh et, quatumsan hendre tincinisi tisisl dolute moloreet atem velesequat alit aliquat, vel dolore faciduis dolore dignis dolorper il eugiamconsed deliquamcon henis alis atum duis at.</p>
    <p>Bore del ute faccum vercill aorper sent alit, venis autet, quipsustio eugue vero dolore velendre euis nos nonse dolessim illa feum dolor sumsan ectet lortincin vulputat amet, qui esto conulput acil in eugait vel essequam zzriusto diam, velit wissit autat.</p>
    <p>Obore dolor incip ea conummy nulput vel ullan henisim am in ute erciliqui ex ent et, quis augiat, commod tis enis num delit laor acing elis dolorer se eugue feu facinci liquis aut lut nulluptat er sum zzrit vulla consequis accum incidunt iusci blaortio odoloreet pratum veliquatie modit, quat. Ut num-modo exercilisl iriliqu ipsusto dolesequat. Ut wisl in ute consequam ad diam vulputpat lan hent vel doloreet utat ver si.</p>
    <p class="letter__new-block">Vullaorem iusci blamcon seniamcommy nit iureetum dolore con ea faccum iureet prat. In utat acidunt nullum venismolum ing exer iusci bla augue magna consequi tem veliquis nostion utpat.</p>
    <p>Nibh euipis esed ero doluptat. Ibh ex exeros exero dolesed dunt pratissi euis nismodipsum eu feugue-rit ipisl incilla faccum am init praese tat velis augue corem iriliqu amconsequat. Magnim ipit in ea acincil esto et wisl esenim volenit lorem del ut aut la commy nibh eui tiniam iure mod tem vel ipisit, quis nonsequi blan exerosto odolorem il irit num vel dolore et irit aute te dolestrud tin hent utet ut praestrud ea faccum venim venim il er iustion sequipsum quat.</p>
    <p class="letter__new-block">Do ea acilisis dolore min ercing endre consequat. Ero consequis ad euguerat, siscidunt laor sum iuscipis nullaoreet, velent ilit amconul laorperit lore diatum dui bla facipit irit alis ad dolorpe rostrud tem essequat praesequam, coreet ip er sim dit, velisim inciliquam, quis adigna feugue dolore et irillaor. Adiam zzrit,</p>
    <p class="letter__sign">Veliquatin Veraessi</p>
  </div>

  <footer class="footer">
    <div class="footer__rule"></div>
    <div class="footer__band">
      <div class="contact">
        <svg viewBox="0 0 10 10" aria-hidden="true"><path fill="currentColor" d="M2 0.5 3.6 2.6 2.7 3.7C3.3 5 4.9 6.6 6.3 7.3L7.4 6.4 9.5 8 8.4 9.5C4.5 9.2.8 5.5.5 1.6Z"/></svg>
        <span>(02) 8371 5926</span>
      </div>
      <div class="contact">
        <svg viewBox="0 0 10 10" aria-hidden="true"><rect x="2.5" y="0.5" width="5" height="3" fill="currentColor"/><rect x="0.5" y="4" width="9" height="4" rx="1" fill="currentColor"/><rect x="2.5" y="7" width="5" height="2.5" fill="currentColor"/></svg>
        <span>(02) 8352 6149</span>
      </div>
      <div class="contact">
        <svg viewBox="0 0 10 10" aria-hidden="true"><rect x="0.5" y="2" width="9" height="6.5" fill="currentColor"/><path d="M0.8 2.3 5 5.8 9.2 2.3" stroke="#b0d03f" stroke-width="1" fill="none"/></svg>
        <span>info@brantorguard.com.au</span>
      </div>
      <div class="contact">
        <svg viewBox="0 0 10 10" aria-hidden="true"><circle cx="5" cy="5" r="4.3" fill="none" stroke="currentColor" stroke-width="1.2"/><path d="M0.7 5h8.6M5 0.7c-2.4 2.6-2.4 6 0 8.6M5 0.7c2.4 2.6 2.4 6 0 8.6" stroke="currentColor" stroke-width="0.8" fill="none"/></svg>
        <span>www.brantorguard.com.au</span>
      </div>
      <div class="contact contact--plain">ACN - 482 617 309</div>
    </div>
  </footer>
</section>

<section class="sheet sheet--follow" aria-label="Follow-on page letterhead">
  <div class="brand">
    <span class="brand__mark"></span>
    <span class="brand__name">Brantor Guard</span>
  </div>

  <div class="letter">
    <p class="letter__salutation">Dear Addressee Name:</p>
    <p>Andipsum dipsum nostis nulpute magnissis niatie te molor adignis sequips uscipisit, sit vel ipsuscing ent lut lan ulla feugait augueraesto odolore doluptatio cons dolor sismodo luptatuero do od dolore magnim dolor auguero eu facilis ea core estrud eugiat velis ad tat dio odolor augue magna corting eugait enim venibh et, quatumsan hendre tincinisi tisisl dolute moloreet atem velesequat alit aliquat, vel dolore faciduis dolore dignis dolorper il eugiamconsed deliquamcon henis alis atum duis at.</p>
    <p>Bore del ute faccum vercill aorper sent alit, venis autet, quipsustio eugue vero dolore velendre euis nos nonse dolessim illa feum dolor sumsan ectet lortincin vulputat amet, qui esto conulput acil in eugait vel essequam zzriusto diam, velit wissit autat.</p>
    <p>Obore dolor incip ea conummy nulput vel ullan henisim am in ute erciliqui ex ent et, quis augiat, commod tis enis num delit laor acing elis dolorer se eugue feu facinci liquis aut lut nulluptat er sum zzrit vulla consequis accum incidunt iusci blaortio odoloreet pratum veliquatie modit, quat. Ut num-modo exercilisl iriliqu ipsusto dolesequat. Ut wisl in ute consequam ad diam vulputpat lan hent vel doloreet utat ver si.</p>
    <p class="letter__new-block">Vullaorem iusci blamcon seniamcommy nit iureetum dolore con ea faccum iureet prat. In utat acidunt nullum venismolum ing exer iusci bla augue magna consequi tem veliquis nostion utpat.</p>
    <p>Nibh euipis esed ero doluptat. Ibh ex exeros exero dolesed dunt pratissi euis nismodipsum eu feugue-rit ipisl incilla faccum am init praese tat velis augue corem iriliqu amconsequat. Magnim ipit in ea acincil esto et wisl esenim volenit lorem del ut aut la commy nibh eui tiniam iure mod tem vel ipisit, quis nonsequi blan exerosto odolorem il irit num vel dolore et irit aute te dolestrud tin hent utet ut praestrud ea faccum venim venim il er iustion sequipsum quat.</p>
    <p class="letter__new-block">Do ea acilisis dolore min ercing endre consequat. Ero consequis ad euguerat, siscidunt laor sum iuscipis nullaoreet, velent ilit amconul laorperit lore diatum dui bla facipit irit alis ad dolorpe rostrud tem essequat praesequam, coreet ip er sim dit, velisim inciliquam, quis adigna feugue dolore et irillaor. Adiam zzrit,</p>
    <p class="letter__sign">Veliquatin Veraessi</p>
  </div>

  <footer class="footer">
    <div class="footer__rule"></div>
    <div class="footer__band"></div>
  </footer>
</section>

</body>
</html>
```